Ayurveda & Wellness Website Redesign.

I need my website www.quilarest.com re-skinned. It is a wordpress site with Divi Builder.
I need a clearer funnel for new clients on the home page.
The funnel should provide questions for the potential client to answer. I can provide these, but I need a better funnel mechanism I think,
Possibly a video on the home page. Or an area of a video that I can change out.
So a better landing page is KEY!
The funnel should reroute to a video page and I should get informed when new clients enroll in the funnel.
Maybe I need a management system for this, but I need a recommendation.
Now I am using forms manager.
I need to be able to make changes using wordpress and/or Divi Builder.
The website should have a clean and spiritual feeling.
I can provide many more pictures and higher resolution.
I like the feeling of this website: http://tarnhollowherbals.com
Also this website: http://calmpetalroots.com/sessionswithorvena/
Target Market(s)
Women ages 25-65. People interested in health, yoga, spirituality.
Industry/Entity Type
Health And Wellness
Coding
Coded - Design and coding required
Requirements
Must have
- A clear sales funnel/enrollment mechanism on the home page. Could have a ebook download (I will provide) when they enroll.
Nice to have
- Currently using Slotra for clients to enroll in appointments. I would like to keep this.

```html
<!DOCTYPE html>
<html lang="en">
<head>
<meta charset="utf-8">
<title>Quila Rest – Ayurveda &amp; Wellness</title>
<link href="https://fonts.googleapis.com/css2?family=Open+Sans:ital,wght@0,400;0,600;0,700;1,400;1,600&display=swap" rel="stylesheet">
<style>
:root{
  --green:#8aa234;
  --green-dark:#6d8423;
  --green-pale:#eef3d9;
  --green-band:#e3ecc4;
  --teal-dark:#06385a;
  --teal:#1f86ad;
  --lilac:#b69ad8;
  --lilac-dark:#8f6fb8;
  --text:#666;
  --text-dark:#333;
  --line:#dcdcdc;
  --card:#f6f6f6;
  --white:#fff;
  --olive:#7e8c52;
}
*{box-sizing:border-box;margin:0;padding:0}
html,body{width:1200px;height:3576px;overflow:hidden}
body{font-family:"Open Sans",Arial,sans-serif;color:var(--text);background:var(--white);font-size:14px;line-height:1.6;position:relative}
.wrap{width:1080px;margin:0 auto;position:relative}

/* top bar */
.top-bar{height:28px;background:var(--green-band);font-size:11px;color:var(--text-dark)}
.top-bar .wrap{display:flex;gap:26px;align-items:center;height:28px}
.top-bar span{display:flex;align-items:center;gap:6px}

/* header */
.site-header{height:102px;background:var(--white);border-bottom:1px solid #eee}
.site-header .wrap{display:flex;align-items:center;justify-content:space-between;height:102px}
.brand{font-size:34px;font-weight:600;color:var(--text-dark);letter-spacing:.5px}
.main-nav{display:flex;gap:26px;align-items:center;font-size:12px;font-weight:600;color:var(--text-dark)}
.main-nav .active{color:var(--teal)}

/* hero */
.hero{height:480px;position:relative;background:radial-gradient(ellipse 380px 240px at 860px 300px,#bfe9f5 0%,#5fbfdc 30%,transparent 70%),linear-gradient(160deg,var(--teal-dark) 0%,#0a5b83 45%,var(--teal) 100%)}
.hero-content{position:absolute;left:185px;top:150px;color:var(--white)}
.hero h1{font-size:30px;font-weight:700;letter-spacing:1px}
.hero p{font-size:24px;margin-top:18px}
.btn-ghost{display:inline-block;margin-top:40px;border:2px solid var(--white);border-radius:4px;padding:10px 22px;font-size:18px}

/* intro */
.intro{padding-top:75px;height:940px;position:absolute;top:610px;left:0;width:1200px}
.section-title{text-align:center;font-style:italic;color:var(--green);font-size:30px;font-weight:400}
.intro-body{display:flex;gap:40px;margin-top:30px}
.intro-body p{width:790px;font-size:14px;line-height:1.65}
.intro-photo{width:230px;height:200px;background:linear-gradient(135deg,#5b2d7a,#b47ac8 55%,#e6d7ee)}

/* assessment */
.assessment{position:absolute;top:1048px;left:0;width:1200px;height:665px;background:linear-gradient(100deg,#fff 0%,#f4f8e6 35%,#e6efcb 70%,#f1f5e1 100%)}
.yoga-photo{position:absolute;left:100px;top:60px;width:260px;height:560px;background:linear-gradient(180deg,#f2f3ec,#d7d6cf 60%,#3a3638 88%,#efefe8)}
.assessment h2{position:absolute;left:460px;top:70px;font-size:15px;font-weight:700;color:var(--teal-dark)}
.assess-form{position:absolute;left:500px;top:112px;width:530px;background:rgba(230,238,200,.75);padding:18px 26px 24px}
.row{display:flex;gap:16px;margin-bottom:14px;align-items:flex-start}
.row label{width:90px;font-size:12px;color:var(--text-dark);padding-top:6px}
.field{background:var(--white);border:1px solid var(--line);height:30px}
.sub{font-size:9px;color:#888;display:block;margin-top:2px}
.btn{display:inline-block;background:var(--lilac);color:var(--white);font-size:13px;font-weight:600;padding:5px 16px;border-radius:3px}
.btn-link{font-size:13px;color:#888;margin-left:14px}

/* testimonials */
.testimonials{position:absolute;top:1730px;left:0;width:1200px;height:690px;background:#fafafa}
.cards{display:flex;justify-content:space-between;width:1020px;margin:40px auto 0}
.card{width:300px;height:620px;background:var(--card);border:1px solid #e6e6e6;position:relative;padding:80px 28px 0;font-size:12.5px;line-height:1.7;color:#777}
.quote-mark{position:absolute;left:50%;top:-22px;transform:translateX(-50%)}
.card .who{margin-top:14px}

/* science */
.science{position:absolute;top:2460px;left:0;width:1200px;height:390px;background:linear-gradient(90deg,#fff 0%,#f4f8e4 40%,#dfe9bc 100%)}
.herbs-photo{position:absolute;left:0;top:40px;width:420px;height:330px;background:radial-gradient(ellipse at 40% 50%,#3f7a2a,#6fa347 40%,#c9d9a6 75%,transparent 90%)}
.science h2{position:absolute;left:520px;top:70px;font-size:28px;font-weight:600;color:var(--green);font-style:italic}
.science-text{position:absolute;left:520px;top:130px;width:600px;font-size:13px;color:var(--green-dark);font-weight:600;line-height:1.65}
.science-text p{margin-bottom:14px}

/* questions */
.questions{position:absolute;top:2985px;left:210px;width:800px;height:160px;background:var(--green-pale);padding:26px 60px}
.q-row{display:flex;align-items:center;gap:20px;margin-bottom:12px;font-size:13px;color:var(--text-dark)}
.q-row span{width:90px}
.select{width:360px;height:26px;background:var(--white);border:1px solid var(--line);font-size:12px;color:#888;padding:3px 8px;display:flex;justify-content:space-between;align-items:center}

/* footer */
.site-footer{position:absolute;top:3230px;left:0;width:1200px;height:296px;background:var(--green-band)}
.footer-cols{display:flex;justify-content:space-between;padding-top:36px}
.footer-col h3{font-size:15px;font-weight:700;color:var(--text-dark);margin-bottom:14px}
.footer-col{font-size:12.5px;color:#555;line-height:1.65}
.footer-col.about{width:320px}
.footer-col.links{width:240px}
.footer-col.contact{width:300px}
.footer-col ul{list-style:none}
.footer-col li::before{content:"• ";}
.bottom-bar{position:absolute;top:3526px;left:0;width:1200px;height:50px;background:var(--olive);color:#eef2dd;font-size:11px;text-align:center;line-height:50px}
</style>
</head>
<body>

<div class="top-bar">
  <div class="wrap">
    <span><svg width="10" height="10" viewBox="0 0 10 10"><path d="M2 1l2 2-1 1.5 2.5 2.5L7 6l2 2-1.5 1.5C4 9 1 6 .5 2.5z" fill="#555"/></svg>707-555-0148</span>
    <span><svg width="12" height="9" viewBox="0 0 12 9"><rect x=".5" y=".5" width="11" height="8" fill="none" stroke="#555"/><path d="M.5.5l5.5 4 5.5-4" fill="none" stroke="#555"/></svg>hello@quilarest.com</span>
  </div>
</div>

<header class="site-header">
  <div class="wrap">
    <div class="brand">Quila Rest</div>
    <nav class="main-nav">
      <span class="active">HOME</span><span>CONSULTS</span><span>AYURVEDA</span><span>ABOUT MAREN</span><span>WORKSHOPS</span><span>FOLLOW THE BLOG</span><span>CONTACT US</span>
      <svg width="14" height="14" viewBox="0 0 14 14"><circle cx="6" cy="6" r="4.5" fill="none" stroke="#555" stroke-width="1.5"/><path d="M9.5 9.5L13 13" stroke="#555" stroke-width="1.5"/></svg>
    </nav>
  </div>
</header>

<section class="hero" role="img" aria-label="Glowing white lotus flower floating on calm blue water">
  <div class="hero-content">
    <h1>QUILA REST WITH AYURVEDA</h1>
    <p>Let our Treatment's warmth work for you!</p>
    <span class="btn-ghost">Get Started Today !</span>
  </div>
</section>

<section class="intro">
  <div class="wrap">
    <h2 class="section-title">Ayurvedic Wellness a year – long course to establish.</h2>
    <div class="intro-body">
      <p>Ayurveda is the "science of life." It is a system of wellness that works with nature to correct imbalances and to maintain balance in the body and spirit. Using the tools of Ayurvedic assessment (including tongue and pulse assessment) we can detect imbalances before they manifest into symptoms. Ayurveda organizes reality into three major categories that are used to understand wellness. These are the doshas, Vata dosha, which is akin to air and ether, is responsible for flows in the body mind: communication, transportation and movement. Ayurveda works to balance these doshas via a variety of modalities including (but not limited to): meditation, nutrition, spices, herbs, herbalized oils, lifestyle recommendations, and aromatherapy. Ayurveda is a powerful system of health and well-being one that allows us to come into resonance with our own true nature.</p>
      <div class="intro-photo" role="img" aria-label="Purple flowers with a small Ayurveda tag"></div>
    </div>
  </div>
</section>

<section class="assessment">
  <div class="yoga-photo" role="img" aria-label="Woman in black seated in a cross-legged meditation pose"></div>
  <h2>Sign Up Here for A Free Ayurvedic Wellness Assessment with Maren Holloway, PhD</h2>
  <div class="assess-form">
    <div class="row"><label>Name<span style="color:#c33">*</span></label>
      <div><div class="field" style="width:170px"></div><span class="sub">First</span></div>
      <div><div class="field" style="width:170px"></div><span class="sub">Last</span></div></div>
    <div class="row"><label>Phone<span style="color:#c33">*</span></label>
      <div><div class="field" style="width:50px"></div><span class="sub">Area</span></div>
      <div><div class="field" style="width:110px"></div><span class="sub">Phone Number</span></div></div>
    <div class="row"><label>E-mail</label><div class="field" style="width:356px"></div></div>
    <div class="row"><label>Message</label><div class="field" style="width:356px;height:100px"></div></div>
    <div class="row" style="align-items:center"><label style="padding:0">Word Verification</label>
      <div class="field" style="width:60px;height:24px;background:#f3efe4;font-size:11px;text-align:center;line-height:22px;color:#555">ykrtza</div>
      <div class="field" style="width:60px;height:24px"></div></div>
    <div style="margin-left:106px;margin-top:20px"><span class="btn">Submit</span><span class="btn-link">Reset</span></div>
  </div>
</section>

<section class="testimonials">
  <div class="cards">
    <article class="card">
      <svg class="quote-mark" width="44" height="44" viewBox="0 0 44 44"><circle cx="22" cy="22" r="21" fill="#fff" stroke="#bbb"/><text x="22" y="32" text-anchor="middle" font-size="26" fill="#888" font-family="Georgia,serif">“</text></svg>
      <p>After Maren's attentive questions, feeling of my pulses and intuitive observation, she prescribed for me a blend of herbs and suggestions for my diet that are simple to keep through the night without my previous flare. I contribute to calming me up. Her blend of humor, humility and insight are a powerful combination. Her very warmth is one that promotes health & ease. I have had private consultations with Maren, and have attended her workshops. I learned each time things that are useful and applicable to my daily life, and am continually charmed by her warmth and kindness.</p>
      <p class="who">(TB)</p>
    </article>
    <article class="card">
      <svg class="quote-mark" width="44" height="44" viewBox="0 0 44 44"><circle cx="22" cy="22" r="21" fill="#fff" stroke="#bbb"/><text x="22" y="32" text-anchor="middle" font-size="26" fill="#888" font-family="Georgia,serif">“</text></svg>
      <p>"It is a pleasure working with Maren as my Ayurvedic practitioner. Her knowledge and expertise is far beyond what I have had before. She is exceptionally knowledgeable, and has a nature gift of sharing information in a way that is easy to understand & simple to apply. With a week of my thorough consultation with Maren, I was experiencing marked & measurable improvements with the issues I was struggling with. I applied her suggestions as well as other lifestyle changes. My life will never be the same & I feel truly thankful. Thanks, Maren!" ~ (CC)</p>
    </article>
    <article class="card">
      <svg class="quote-mark" width="44" height="44" viewBox="0 0 44 44"><circle cx="22" cy="22" r="21" fill="#fff" stroke="#bbb"/><text x="22" y="32" text-anchor="middle" font-size="26" fill="#888" font-family="Georgia,serif">“</text></svg>
      <p>"Maren is an attentive and insightful practitioner. The depth and breadth of her studies of Indian culture, yoga and health, academic and practical, is a proud wellspring. She has a compassionate manner, and is generous with her time and knowledge. All of these things combine to make Maren an extraordinary resource. I am exceedingly grateful for her help." ~ (TJ)</p>
    </article>
  </div>
</section>

<section class="science">
  <div class="herbs-photo" role="img" aria-label="Mortar and pestle with fresh green herbs"></div>
  <h2>Ayurveda 'Science of Life'</h2>
  <div class="science-text">
    <p>Ayurveda is a science and art of appropriate living which helps to achieve longevity. It can also guide every individual in the prevention of diseases and long term maintenance of health.</p>
    <p>Samadosha, samagnischa, samadhatu malakriyah Prasanna atma indriya manah swastha iti abhidheeyate. Sushruta Samhita 15/38</p>
    <p>"One who is established in Self, who has balanced doshas, balanced agni, balanced tissues, properly formed dhatus, proper elimination of wastes, well functioning bodily processes and whose mind, soul and senses are full of bliss, is called a healthy person."</p>
  </div>
</section>

<section class="questions">
  <div class="q-row"><span>Question1:</span><div class="select">select 1<svg width="8" height="10" viewBox="0 0 8 10"><path d="M1 4l3-3 3 3M1 6l3 3 3-3" fill="none" stroke="#777"/></svg></div></div>
  <div class="q-row"><span>Question2:</span><div class="select">Select none<svg width="8" height="10" viewBox="0 0 8 10"><path d="M1 4l3-3 3 3M1 6l3 3 3-3" fill="none" stroke="#777"/></svg></div></div>
  <div><span class="btn" style="background:var(--lilac-dark)">Submit</span><span class="btn-link">Reset</span></div>
</section>

<footer class="site-footer">
  <div class="wrap footer-cols">
    <div class="footer-col about">
      <h3>About Maren</h3>
      <p>I am passionate about energy renewal and helping people receive their health imbalances. Maren has been studying and learning about Ayurveda for many years and have studied Clinical Ayurveda, Ayurvedic Spiritual Counseling and Jyotish (Vedic Astrology) under Dr. Elan Marsh of Tarn Hollow Ayurveda.</p>
    </div>
    <div class="footer-col links">
      <h3>Quick Links</h3>
      <ul><li>About Maren</li><li>Consults</li><li>Ayurveda</li><li>Workshops</li></ul>
    </div>
    <div class="footer-col contact">
      <h3>Contact Us</h3>
      <p>Tel : +707-555-0148</p>
      <p style="margin-top:10px">Email : hello@quilarest.com</p>
    </div>
  </div>
</footer>
<div class="bottom-bar">© 2016 Quila Rest. All Rights Reserved.</div>

</body>
</html>
```